Business cards for veterinary clinic

Hi, We are looking for business cards to be designed for our other veterinary clinic. We were very happy with the design done for our other clinic a few months ago. We already have a logo for use which I will attach (please use the image not the text around.
We need a couple of different cards (same design with different names on them) produced

Industry/Entity Type

Veterinary

Contact Information for Business Card

Mossvale Creek Vet Clinic
58 Orchard Rd
Wattle Glen
VIC 3571
03) 5812 4396
clinic@mossvalecreekvetclinic.com.au

Font styles to use
Sans Serif

Colors
0455a3
0592cd

Requirements
Must have
• Three different names
• 1. Generic (no name) with email clinic@mossvalecreekvetclinic.com.au
• 2. Leonie Pratt -Director with email leonie@mossvalecreekvetclinic.com.au
• 3. Declan Hume - Vet Director with email leonie@mossvalecreekvetclinic.com.au

```html
<!DOCTYPE html>
<html lang="en">
<head>
<meta charset="utf-8">
<title>Mossvale Creek Vet Clinic — Business Cards</title>
<link href="https://fonts.googleapis.com/css2?family=Jost:wght@400;500&display=swap" rel="stylesheet">
<style>
  :root {
    --navy: #0455a3;
    --deep: #234a8f;
    --sky: #0592cd;
    --aqua: #7ecfe0;
    --rule: #5cc3dc;
    --paper: #fbfbfa;
    --backdrop: #1c2a3c;
  }
  * { box-sizing: border-box; margin: 0; padding: 0; }
  html, body { width: 1200px; height: 1000px; overflow: hidden; }
  body {
    background: var(--backdrop);
    font-family: "Jost", "Futura", sans-serif;
    display: flex;
    align-items: center;
    justify-content: center;
    gap: 80px;
  }
  .card {
    width: 440px;
    height: 760px;
    border-radius: 4px;
    overflow: hidden;
    position: relative;
  }
  .card-front {
    background: var(--paper);
    padding: 70px 40px 0;
    text-transform: uppercase;
  }
  .brand {
    display: flex;
    flex-direction: column;
    align-items: center;
    gap: 22px;
  }
  .brand-dot {
    width: 150px;
    height: 150px;
    border-radius: 50%;
    background: var(--aqua);
  }
  .brand-name {
    color: var(--aqua);
    font-weight: 400;
    font-size: 37px;
    line-height: 1.05;
    text-align: center;
    letter-spacing: 0.5px;
  }
  .rule { border: 0; border-top: 2px solid var(--rule); margin: 22px 6px; }
  .person { text-align: center; }
  .person-name {
    color: var(--deep);
    font-weight: 500;
    font-size: 40px;
    line-height: 1;
    letter-spacing: 1px;
  }
  .person-role { color: var(--sky); font-size: 17px; letter-spacing: 1px; }
  .phone {
    color: var(--deep);
    font-size: 62px;
    font-weight: 400;
    text-align: center;
    line-height: 1;
    letter-spacing: 2px;
  }
  .contact {
    color: var(--deep);
    font-style: normal;
    font-size: 15px;
    text-align: center;
    line-height: 1.45;
    letter-spacing: 1px;
  }
  .contact .email {
    display: block;
    font-size: 14.5px;
    letter-spacing: 0.4px;
    white-space: nowrap;
  }
  .card-back { background: var(--navy); }
  .back-art { position: absolute; inset: 0; }
</style>
</head>
<body>
  <article class="card card-front">
    <header class="brand">
      <div class="brand-dot"></div>
      <h1 class="brand-name">Mossvale Creek<br>Vet Clinic</h1>
    </header>
    <hr class="rule">
    <div class="person">
      <h2 class="person-name">Leonie Pratt</h2>
      <p class="person-role">Director</p>
    </div>
    <hr class="rule">
    <p class="phone">5812 4396</p>
    <hr class="rule">
    <address class="contact">
      58 Orchard Rd Wattle<br>
      Glen VIC 3571<br>
      <span class="email">leonie@mossvalecreekvetclinic.com.au</span>
    </address>
    <hr class="rule">
  </article>

  <article class="card card-back">
    <svg class="back-art" viewBox="0 0 440 760" role="img" aria-label="Silhouettes of a horse, cow, dog and cat in shades of blue inside a white arch">
      <defs>
        <linearGradient id="arch-fill" x1="0" y1="0" x2="0" y2="1">
          <stop offset="0" stop-color="#ffffff"/>
          <stop offset="0.45" stop-color="#7ecfe0"/>
          <stop offset="1" stop-color="#0592cd"/>
        </linearGradient>
      </defs>
      <path d="M0 420 Q220 300 440 420 L440 760 L0 760 Z" fill="var(--rule)"/>
      <path d="M0 432 Q220 316 440 432 L440 760 L0 760 Z" fill="url(#arch-fill)"/>
    </svg>
  </article>
</body>
</html>
```